Letterhead Design Project for online gaming site

We need a letterhead for a new online gaming company. The site is www.lunaroller.co

The logo is a gold colour and the site is similar in nature. Feel free to take a look at the landing page.

However the designer has free reign to do whatever they like with it.

OTHER CONTENT:

Telephone: 1300 746 315
Email: info@lunaroller.co
Web: www.lunaroller.co

Industry/Entity Type

It Company

```html
<!DOCTYPE html>
<html lang="en">
<head>
<meta charset="utf-8">
<title>LunaRoller.co Letterhead</title>
<link rel="stylesheet" href="https://fonts.googleapis.com/css2?family=Arimo:wght@400;700&family=Sorts+Mill+Goudy&family=Share+Tech+Mono&display=swap">
<style>
  :root {
    --backdrop: #e4e4e4;
    --paper: #ffffff;
    --gold: #d9a91c;
    --gold-label: #c29a2e;
    --ink: #333333;
    --body-ink: #4a4a4a;
    --rule: #9a9a9a;
    --silhouette: #ebebeb;
    --band-yellow: #fcd20a;
    --band-brown: #8f7533;
    --band-ink: #3a3220;
  }
  * { margin: 0; padding: 0; box-sizing: border-box; }
  html, body { width: 1200px; height: 750px; overflow: hidden; }
  body { background: var(--backdrop); position: relative; font-family: "Arimo", Arial, sans-serif; }

  .sheet { position: absolute; background: var(--paper); overflow: hidden; }
  .sheet--first { left: 180px; top: 75px; width: 422px; height: 597px; }
  .sheet--follow { left: 654px; top: 75px; width: 422px; height: 602px; }

  .brand-name {
    position: absolute; font-family: "Arimo", Arial, sans-serif; font-weight: 700;
    color: var(--gold); letter-spacing: -0.5px; white-space: nowrap;
  }
  .sheet--first .brand-name { left: 0; right: 0; top: 17px; text-align: center; font-size: 27px; }
  .sheet--follow .brand-name { right: 13px; top: 57px; font-size: 20px; }

  .head-rule { position: absolute; height: 1px; background: var(--rule); }
  .sheet--first .head-rule { left: 16px; right: 14px; top: 52px; }
  .sheet--follow .head-rule { left: 16px; right: 14px; top: 81px; }

  .contact {
    position: absolute; left: 0; right: 0; top: 55px; text-align: center;
    font-family: "Sorts Mill Goudy", Georgia, serif; font-size: 8px; line-height: 11px; color: var(--ink);
  }
  .contact .label { color: var(--gold-label); }
  .contact .item { margin: 0 2px; }

  .letter { position: absolute; left: 25px; width: 383px; top: 154px; color: var(--body-ink); font-size: 6.8px; line-height: 14.6px; }
  .letter .greeting { font-weight: 700; color: var(--ink); margin-bottom: 13px; }
  .letter p { margin-bottom: 13px; }

  .racing-art { position: absolute; background: linear-gradient(90deg, var(--silhouette), #f1f1f1); border-radius: 40px 60px 0 0; }
  .sheet--first .racing-art { left: 36px; top: 462px; width: 340px; height: 104px; }
  .sheet--follow .racing-art { left: 23px; top: 14px; width: 203px; height: 66px; border-radius: 30px 40px 4px 4px; }

  .page-count {
    position: absolute; right: 17px; top: 21px;
    font-family: "Sorts Mill Goudy", Georgia, serif; font-size: 8.5px; color: #555;
  }
  .page-count .blank { display: inline-block; width: 24px; border-bottom: 1px solid #777; margin: 0 1px; }

  .tagline-band {
    position: absolute; left: 0; right: 0; height: 23px;
    font-family: "Share Tech Mono", "Courier New", monospace; font-size: 10px;
    letter-spacing: 1.5px; color: var(--band-ink); line-height: 23px; padding-left: 30px; white-space: nowrap;
  }
  .sheet--first .tagline-band { top: 566px; background: linear-gradient(90deg, var(--band-brown) 0%, #b4962a 35%, var(--band-yellow) 75%); }
  .sheet--follow .tagline-band { top: 577px; background: linear-gradient(90deg, var(--band-yellow) 20%, #c9a624 60%, var(--band-brown) 100%); }
</style>
</head>
<body>

<section class="sheet sheet--first">
  <div class="brand-name">LunaRoller.co</div>
  <div class="head-rule"></div>
  <div class="contact">
    <div>
      <span class="item"><span class="label">Telephone:</span> 1300 746 315</span>
      <span class="item"><span class="label">Email:</span> info@lunaroller.co</span>
    </div>
    <div><span class="label">Web:</span> www.lunaroller.co</div>
  </div>

  <div class="letter">
    <div class="greeting">Dear Customer,</div>
    <p>Lorem ipsum dolor sit amet, consectetur adipiscing elit. Donec elementum velit sit amet libero fringilla adipiscing. Aliquam sollicitudin, leo vitae molestie facilisis, tellus ligula varius velit, vitae tincidunt lacus purus vitae nulla. Nulla imperdiet, odio quis ultrices ornare, diam est dictum lacus, et vehicula est magna at metus. Integer mattis lorem quis tortor accumsan ultrices ac ut massa. Duis eget metus ut risus scelerisque ornare quis eget dui. Aliquam lobortis dolor vitae magna volutpat eu facilisis tellus molestie. Sed a purus quis nibh lacinia interdum ut at leo.</p>
    <p>Integer consequat velit quis elit hendrerit imperdiet. Donec felis velit, volutpat vel convallis nec, sollicitudin et nulla. Pellentesque sodales elementum aliquam. Donec convallis, turpis sit amet laoreet ultricies, enim est elementum magna, dictum lobortis eros tellus quis diam. Nunc suscipit augue non nisl volutpat volutpat. Ut egestas ultrices purus, eget varius nibh placerat in. Cras leo ante, congue id ultricies a, ornare eu est. Curabitur eleifend tincidunt mi eget tristique.</p>
    <p>Etiam arcu augue, ornare vitae consectetur luctus, tincidunt vitae urna. Lorem ipsum dolor sit amet, consectetur adipiscing elit. Donec vitae tortor quis orci adipiscing lobortis. Morbi aliquet orci quis mi viverra sollicitudin. Sed eget pellentesque turpis. Aliquam commodo sodales ultrices. Nullam ut elit vitae elit suscipit porttitor viverra non mi. Donec diam mi, tincidunt nec sodales vestibulum, iaculis a urna. Nulla facilisi.</p>
    <p>Thanking you,</p>
  </div>

  <div class="racing-art" role="img" aria-label="Faint grey silhouettes of a harness racer, a galloping thoroughbred with jockey, greyhounds and a football"></div>
  <div class="tagline-band">THOROUGHBRED HARNESS GREYHOUND &nbsp;SPORT AND LAY BETTING</div>
</section>

<section class="sheet sheet--follow">
  <div class="racing-art" role="img" aria-label="Faint grey silhouettes of a harness racer, racehorses, greyhounds and a football"></div>
  <div class="page-count">Page:<span class="blank"></span>Of<span class="blank"></span></div>
  <div class="brand-name">LunaRoller.co</div>
  <div class="head-rule"></div>
  <div class="tagline-band">THOROUGHBRED HARNESS GREYHOUND &nbsp;SPORT AND LAY BETTING</div>
</section>

</body>
</html>
```